Carpentry and Building Business Card

I'm looking for a business card that is minimalistic and that incorporates the theme of my Velmor logo.
On one side I'd like the VELMOR logo with my details on the other side.
Double sided with curved edges

Target Market(s)

Construction / renovation
Adults

Industry/Entity Type

Tradesman

Contact Information for Business Card

Logo on one side, details on the other

Colors

Designer to choose only greyscale colors for use in the design.

Requirements
Must have
• Nilo Petrakis
VELMOR CONSTRUCT
Carpentry & Building Services
0481236574
Velmorconstruct@brixmail.com
Lic No. 718263D
Nice to have
• Fb and insta icons. @velmorconstruct
Should not have
• No hammer or tool icons please.

No address line.

```html
<!DOCTYPE html>
<html lang="en">
<head>
<meta charset="utf-8">
<title>Velmor Business Card</title>
<link href="https://fonts.googleapis.com/css2?family=Arimo:wght@400;700&display=swap" rel="stylesheet">
<style>
  :root {
    --page: #ececec;
    --card-light: #ffffff;
    --card-dark: #222222;
    --accent: #d8913f;
    --ink: #333333;
    --paper-text: #ffffff;
  }
  * { margin: 0; padding: 0; box-sizing: border-box; }
  html, body { width: 1200px; height: 915px; overflow: hidden; background: var(--page); }
  .canvas { position: relative; width: 1200px; height: 915px; }

  .card { position: absolute; left: 276px; width: 651px; height: 377px; border-radius: 20px; overflow: hidden; }
  .card--front { top: 59px; background: var(--card-light); }
  .card--back { top: 465px; background: var(--card-dark); display: flex; align-items: center; justify-content: center; }

  .edge-stripe { position: absolute; top: 0; right: 0; width: 11px; height: 100%; background: var(--card-dark); }
  .edge-stripe__accent { position: absolute; right: 0; top: 180px; width: 11px; height: 39px; background: var(--accent); border-top: 2px solid var(--card-light); border-bottom: 2px solid var(--card-light); }

  .brand { display: flex; align-items: center; }
  .brand__square { flex: none; border: 3px solid var(--accent); }
  .brand__name { font-family: "Arimo", sans-serif; font-weight: 700; line-height: 1; letter-spacing: 0; }

  .card--front .brand { position: absolute; left: 20px; top: 68px; gap: 16px; }
  .card--front .brand__square { width: 44px; height: 44px; border-width: 2px; }
  .card--front .brand__name { font-size: 38px; color: var(--card-dark); }

  .card--back .brand { gap: 24px; }
  .card--back .brand__square { width: 64px; height: 64px; }
  .card--back .brand__name { font-size: 52px; color: var(--paper-text); }

  .identity { position: absolute; right: 22px; top: 172px; text-align: right; font-family: "Arimo", sans-serif; }
  .identity__name { font-size: 28px; font-weight: 700; color: var(--accent); line-height: 30px; }
  .identity__role { font-size: 16.5px; color: var(--ink); line-height: 20px; }

  .contact { position: absolute; left: 20px; top: 264px; font-family: "Arimo", sans-serif; font-size: 16.5px; color: var(--ink); }
  .contact__licence { line-height: 22px; margin-bottom: 7px; }
  .contact__line { display: flex; align-items: center; gap: 7px; line-height: 22px; }
  .contact__icon { width: 12px; height: 12px; flex: none; }
</style>
</head>
<body>
<main class="canvas">
  <section class="card card--front" aria-label="Business card front">
    <div class="brand">
      <span class="brand__square"></span>
      <span class="brand__name">Velmor</span>
    </div>
    <div class="identity">
      <p class="identity__name">Nilo Petrakis</p>
      <p class="identity__role">Carpentry &amp; Building Services</p>
    </div>
    <div class="contact">
      <p class="contact__licence">Lic No. 718263D</p>
      <p class="contact__line">
        <svg class="contact__icon" viewBox="0 0 24 24" aria-hidden="true"><path fill="#d8913f" d="M6.6 10.8c1.4 2.8 3.8 5.1 6.6 6.6l2.2-2.2c.3-.3.7-.4 1-.2 1.1.4 2.3.6 3.6.6.6 0 1 .4 1 1V20c0 .6-.4 1-1 1C10.6 21 3 13.4 3 4c0-.6.4-1 1-1h3.5c.6 0 1 .4 1 1 0 1.3.2 2.5.6 3.6.1.3 0 .7-.2 1z"/></svg>
        <span>0481236574</span>
      </p>
      <p class="contact__line">
        <svg class="contact__icon" viewBox="0 0 24 24" aria-hidden="true"><rect x="1" y="5" width="22" height="14" fill="#d8913f"/><path d="M2 6l10 7 10-7" fill="none" stroke="#ffffff" stroke-width="2"/></svg>
        <span>Velmorconstruct@brixmail.com</span>
      </p>
    </div>
    <div class="edge-stripe"><span class="edge-stripe__accent"></span></div>
  </section>

  <section class="card card--back" aria-label="Business card back">
    <div class="brand">
      <span class="brand__square"></span>
      <span class="brand__name">Velmor</span>
    </div>
  </section>
</main>
</body>
</html>
```